Project Title:
Dental Implant Overdenture Flyer (Retirement Village Target)
Objective:
Create a clean, trustworthy, and reassuring flyer aimed at older adults (60–85 years old) who struggle with loose dentures. The goal is to educate them about implant-retained “clip-on” dentures and encourage them to book a consultation.
Tone & Feel:
Warm, caring, non-intimidating
Premium but not “salesy”
Medical but easy to understand
Focus on improving quality of life (confidence, eating, comfort)
Target Audience:
Retirees / pensioners
Existing denture wearers
People frustrated with loose or uncomfortable dentures
Key Message:
“You don’t have to live with loose dentures anymore.”
Design Style:
Clean, minimal, modern
Soft colours (blues, greens, warm neutrals)
Easy-to-read large font
High contrast for older eyes
Avoid clutter
Imagery Suggestions:
Smiling older adults (natural, not stocky/overly staged)
Before/after lifestyle (eating, laughing, socialising)
Simple diagram showing denture clipping onto implants
Avoid graphic surgical images
Layout Suggestions:
A5 or DL flyer
Clear sections with headings
Icons for benefits
Strong call-to-action at bottom
HEADLINE (big and bold)
Tired of Loose Dentures?
Discover Secure “Clip-On” Teeth
🔹 PROBLEM SECTION
Do your dentures:
Slip or move when eating?
Make it hard to chew certain foods?
Feel uncomfortable or loose?
Affect your confidence when speaking or smiling?
You’re not alone — and there is a better solution.
🔹 SOLUTION SECTION
Implant-Retained “Clip-On” Dentures
We can secure your denture using just 2 dental implants, allowing your teeth to:
✔ Stay firmly in place
✔ Improve your ability to eat
✔ Feel more comfortable
✔ Boost your confidence
🔹 SIMPLE EXPLANATION (very important)
Small titanium implants are gently placed in the jaw.
Your denture then clips securely onto them, stopping movement.
🔹 PRICE SECTION (highlight this clearly)
$12,000
Includes:
2 dental implants
A brand new custom overdenture
Does not include sedation or extractions (if needed)
🔹 SEDATION
Sedation is available for comfort.
If you hold a pensioner card, you may receive a significant Vantacor rebate, often resulting in minimal out-of-pocket costs for sedation.
🔹 TRUST / REASSURANCE
Experienced implant clinician
Gentle, patient-focused care
Modern technology and techniques
🔹 CALL TO ACTION (VERY IMPORTANT)
Book a Free Consultation
📞 Call: 08 9351 4276
🌐 Visit: www.bravonclinic.com.au
📍 Located near Tallowmere shopping centre
🔹 OPTIONAL TAGLINE
Eat Better. Feel Better. Smile with Confidence Again.
Please include some photos to illustrate what a clip on denture looks like with two implants.

```html
<!DOCTYPE html>
<html lang="en">
<head>
<meta charset="utf-8">
<title>Clip-On Dentures Flyer – Bravon Clinic</title>
<link rel="stylesheet" href="https://fonts.googleapis.com/css2?family=Poppins:ital,wght@0,400;0,500;0,600;0,700;0,800;1,400&display=swap">
<style>
:root{
  --teal:#1591a8;
  --teal-dark:#0f8aa3;
  --teal-light:#33d0c5;
  --ink:#111111;
  --grey-text:#5a5a5a;
  --muted:#a9a9a9;
  --card:#eeeeee;
  --band:#efefef;
  --white:#ffffff;
}
*{margin:0;padding:0;box-sizing:border-box}
html,body{width:845px;height:1200px;overflow:hidden;background:var(--white)}
body{font-family:"Poppins",sans-serif;color:var(--ink)}
.flyer{position:relative;width:845px;height:1200px;overflow:hidden;background:var(--white)}

.hero-art{position:absolute;left:0;top:0;width:845px;height:360px}
.brand{position:absolute;left:52px;top:58px;display:flex;align-items:center;gap:10px}
.brand-dot{width:34px;height:34px;border-radius:50%;background:var(--teal)}
.brand-name{font-size:20px;font-weight:600;color:var(--teal);letter-spacing:.5px}

.headline{position:absolute;left:48px;top:120px;font-size:62px;line-height:60px;letter-spacing:-.5px;font-weight:400}
.headline strong{font-weight:800}
.subhead{position:absolute;left:49px;top:256px;font-size:22px;font-weight:400}
.subhead strong{font-weight:700}

.rule-faint{position:absolute;left:0;top:443px;width:845px;height:1px;background:#d6eef1}

.problem{position:absolute;left:50px;top:370px;width:440px}
.section-title{font-size:21px;font-weight:700;line-height:1.2}
.dot-list{list-style:none;margin-top:10px}
.dot-list li{position:relative;padding-left:22px;font-size:17.5px;line-height:24px;margin-bottom:0}
.dot-list li::before{content:"";position:absolute;left:0;top:9px;width:7px;height:7px;border-radius:50%;background:var(--teal)}
.callout{margin-top:14px;font-size:20px;font-weight:700;color:var(--teal);line-height:23px}

.divider{position:absolute;left:45px;top:628px;width:455px;border-top:1.5px dashed #d3d3d3}

.solution{position:absolute;left:50px;top:646px;width:460px}
.solution .section-title{font-size:21.5px}
.solution .section-title em{font-style:normal;color:var(--teal)}
.solution-intro{margin-top:12px;font-size:17.5px;line-height:20px}
.tick-list{list-style:none;margin-top:10px}
.tick-list li{display:flex;align-items:center;gap:10px;font-size:17.5px;line-height:24px}
.tick-list svg{flex:none}

.lifestyle{position:absolute;top:853px;width:181px;height:87px;border-radius:16px;background:linear-gradient(120deg,#6b5a45 0%,#b7a189 45%,#e2d3c2 70%,#8c7a64 100%)}
.lifestyle.one{left:48px}
.lifestyle.two{left:241px}

.how{position:absolute;left:528px;top:367px;width:263px}
.how-title{font-size:19px;font-weight:700;color:var(--muted);letter-spacing:.3px}
.step{display:flex;align-items:center;gap:22px;margin-top:12px;height:88px;padding:0 10px 0 20px;background:var(--card);border-radius:6px}
.step + .step{margin-top:4px}
.step-visual{flex:none;width:84px;height:64px;border-radius:4px;border:1px solid #cfcfcf;background:linear-gradient(180deg,#e9f2f7 0%,#c9dfec 55%,#f3c9c5 100%)}
.step-text{font-size:13.5px;line-height:15px}

.price-box{position:absolute;left:529px;top:619px;width:262px;height:199px;border:1.5px dashed var(--teal-light);border-radius:18px;padding:20px 24px 0 25px}
.scissors{position:absolute;left:112px;top:-12px;background:var(--white);padding:0 4px}
.price{font-size:48px;font-weight:800;color:var(--teal);line-height:54px;letter-spacing:-.5px}
.includes{margin-top:8px;font-size:14px;line-height:16.5px;color:#555}
.includes strong{display:block;font-weight:700;color:#444}

.sedation{position:absolute;left:528px;top:843px;width:270px}
.sedation-title{font-size:15px;font-weight:700;color:var(--teal)}
.sedation-text{margin-top:6px;font-size:12.8px;line-height:14.5px;color:#222}

.trust-band{position:absolute;left:0;top:957px;width:845px;height:101px;background:var(--band)}
.trust{position:absolute;top:18px;display:flex;align-items:center;gap:20px}
.trust.one{left:50px}
.trust.two{left:297px}
.trust.three{left:553px}
.trust-icon{width:68px;height:68px;border-radius:50%;border:1.5px dashed var(--teal);display:flex;align-items:center;justify-content:center;flex:none}
.trust-label{font-size:15px;line-height:14px;color:#222}

.cta-band{position:absolute;left:0;top:1058px;width:845px;height:75px;background:var(--teal-dark)}
.cta-button{position:absolute;left:47px;top:19px;width:359px;height:43px;border-radius:10px;background:#000;color:var(--white);font-size:22.5px;line-height:43px;padding-left:34px}
.phone-icon{position:absolute;left:465px;top:16px;width:34px;height:34px;border-radius:50%;background:var(--teal-light);display:flex;align-items:center;justify-content:center}
.phone-number{position:absolute;left:512px;top:6px;font-size:37px;font-weight:800;color:var(--white);letter-spacing:.3px}
.cta-meta{position:absolute;left:465px;top:55px;font-size:10.5px;font-weight:600;color:var(--white)}

.tagline{position:absolute;left:0;top:1146px;width:845px;text-align:center;font-size:20px;font-style:italic;color:var(--grey-text)}
</style>
</head>
<body>
<main class="flyer">

  <svg class="hero-art" viewBox="0 0 845 360" aria-hidden="false">
    <defs>
      <linearGradient id="portraitTone" x1="0" y1="0" x2="1" y2="0">
        <stop offset="0" stop-color="#ffffff"/>
        <stop offset=".25" stop-color="#efe6dc"/>
        <stop offset=".6" stop-color="#d8b9a0"/>
        <stop offset="1" stop-color="#b9967c"/>
      </linearGradient>
      <clipPath id="portraitClip">
        <path d="M380 0 H845 V128 C720 250 560 335 300 348 L380 0 Z"/>
      </clipPath>
    </defs>
    <g role="img" aria-label="Photo of a smiling senior man with confident natural teeth">
      <rect x="380" y="0" width="465" height="360" fill="url(#portraitTone)" clip-path="url(#portraitClip)"/>
    </g>
    <path d="M0 290 C120 315 220 340 360 346 C520 352 700 290 845 205 L845 228 C700 310 520 356 360 356 C220 356 100 350 0 344 Z" fill="var(--teal-light)"/>
    <path d="M270 349 C520 346 700 265 845 122 L845 222 C700 305 520 352 320 352 Z" fill="var(--teal)"/>
  </svg>

  <div class="brand">
    <span class="brand-dot"></span>
    <span class="brand-name">Bravon Clinic</span>
  </div>

  <h1 class="headline">Tired of <strong>Loose</strong><br><strong>Dentures?</strong></h1>
  <p class="subhead">Discover Secure <strong>“Clip-On”</strong> Teeth</p>

  <div class="rule-faint"></div>

  <section class="problem">
    <h2 class="section-title">Do your dentures</h2>
    <ul class="dot-list">
      <li>Slip or move when eating?</li>
      <li>Make it hard to chew certain foods?</li>
      <li>Make it hard to chew certain foods?</li>
      <li>Feel uncomfortable or loose?</li>
      <li>Affect your confidence when speaking or smiling?</li>
    </ul>
    <p class="callout">You’re not alone and there is a<br>better solution.</p>
  </section>

  <div class="divider"></div>

  <section class="solution">
    <h2 class="section-title">Implant-Retained <em>“Clip-On”</em> Dentures</h2>
    <p class="solution-intro">We can secure your denture using just 2 dental implants, allowing your teeth to:</p>
    <ul class="tick-list">
      <li><svg width="14" height="14" viewBox="0 0 14 14"><circle cx="7" cy="7" r="6" fill="none" stroke="var(--teal)" stroke-width="1.4"/><path d="M4 7.2 6.2 9.3 11.5 3.5" fill="none" stroke="var(--teal)" stroke-width="1.8" stroke-linecap="round"/></svg>Stay firmly in place</li>
      <li><svg width="14" height="14" viewBox="0 0 14 14"><circle cx="7" cy="7" r="6" fill="none" stroke="var(--teal)" stroke-width="1.4"/><path d="M4 7.2 6.2 9.3 11.5 3.5" fill="none" stroke="var(--teal)" stroke-width="1.8" stroke-linecap="round"/></svg>Improve your ability to eat</li>
      <li><svg width="14" height="14" viewBox="0 0 14 14"><circle cx="7" cy="7" r="6" fill="none" stroke="var(--teal)" stroke-width="1.4"/><path d="M4 7.2 6.2 9.3 11.5 3.5" fill="none" stroke="var(--teal)" stroke-width="1.8" stroke-linecap="round"/></svg>Feel more comfortable</li>
      <li><svg width="14" height="14" viewBox="0 0 14 14"><circle cx="7" cy="7" r="6" fill="none" stroke="var(--teal)" stroke-width="1.4"/><path d="M4 7.2 6.2 9.3 11.5 3.5" fill="none" stroke="var(--teal)" stroke-width="1.8" stroke-linecap="round"/></svg>Boost your confidence</li>
    </ul>
  </section>

  <div class="lifestyle one" role="img" aria-label="Photo of a senior woman laughing in her kitchen"></div>
  <div class="lifestyle two" role="img" aria-label="Photo of a senior woman smiling comfortably at home"></div>

  <section class="how">
    <h2 class="how-title">HOW IT WORKS</h2>
    <div class="step">
      <div class="step-visual" role="img" aria-label="Diagram of two titanium implants placed in the lower jaw"></div>
      <p class="step-text">Small titanium implants are gently placed in the jaw.</p>
    </div>
    <div class="step">
      <div class="step-visual" role="img" aria-label="Diagram of a denture clipping onto two implants"></div>
      <p class="step-text">Your denture then clips securely onto them, stopping movement.</p>
    </div>
  </section>

  <section class="price-box">
    <svg class="scissors" width="30" height="22" viewBox="0 0 30 22" aria-hidden="true">
      <circle cx="6" cy="5" r="3.5" fill="none" stroke="#111" stroke-width="2"/>
      <circle cx="6" cy="17" r="3.5" fill="none" stroke="#111" stroke-width="2"/>
      <path d="M9 7 L27 17 M9 15 L27 5" stroke="#111" stroke-width="2" stroke-linecap="round"/>
    </svg>
    <p class="price">$12,000</p>
    <p class="includes">INCLUDES:
      <strong>2 dental implants</strong>
      <strong>A brand new custom overdenture</strong>
      Does not include sedation or extractions (if needed)</p>
  </section>

  <section class="sedation">
    <h3 class="sedation-title">Sedation is available for comfort.</h3>
    <p class="sedation-text">If you hold a pensioner card, you may receive a significant Vantacor rebate, often resulting in minimal out-of-pocket costs for sedation.</p>
  </section>

  <section class="trust-band">
    <div class="trust one">
      <div class="trust-icon">
        <svg width="40" height="40" viewBox="0 0 40 40" fill="none" stroke="#222" stroke-width="1.6" stroke-linejoin="round"><path d="M8 8c4-4 8-2 11 0 4-2 8-3 11 1 3 4 1 10-1 13-1 4-1 13-4 13-3 0-2-9-6-9s-3 9-6 9c-3 0-3-9-4-13C7 19 5 12 8 8Z"/><path d="M26 16h4v4h4v4h-4v4h-4v-4h-4v-4h4Z" fill="#fff"/></svg>
      </div>
      <p class="trust-label">Experienced<br>implant clinician</p>
    </div>
    <div class="trust two">
      <div class="trust-icon">
        <svg width="40" height="40" viewBox="0 0 40 40" fill="none" stroke="#222" stroke-width="1.6" stroke-linejoin="round" stroke-linecap="round"><path d="M14 8c2-2 4-1 6 0 2-1 4-2 6 0s1 6 0 8c0 3-1 8-3 8s-1-5-3-5-1 5-3 5-3-5-3-8c-1-2-2-6 0-8Z"/><path d="M5 18v8l8 8v3M35 18v8l-8 8v3M9 22l5 6M31 22l-5 6"/></svg>
      </div>
      <p class="trust-label">Gentle, patient-<br>focused care</p>
    </div>
    <div class="trust three">
      <div class="trust-icon">
        <svg width="40" height="40" viewBox="0 0 40 40" fill="none" stroke="#222" stroke-width="1.6" stroke-linejoin="round" stroke-linecap="round"><rect x="5" y="6" width="30" height="22" rx="2"/><path d="M16 28v5M24 28v5M12 34h16"/><path d="M12 11c2-1.5 3-1 4.5 0 1.5-1 3-1.5 4.5 0s.5 4 0 5c0 2-.5 5-2 5s-1-3-2.5-3-1 3-2.5 3-2-3-2-5c-.5-1-1-3.5 0-5Z"/><path d="M28 12v.5M28 15v7"/></svg>
      </div>
      <p class="trust-label">Modern technology<br>and techniques</p>
    </div>
  </section>

  <section class="cta-band">
    <div class="cta-button">Book a Free Consultation</div>
    <div class="phone-icon">
      <svg width="18" height="18" viewBox="0 0 24 24" aria-hidden="true"><path d="M6.6 10.8a15 15 0 0 0 6.6 6.6l2.2-2.2a1 1 0 0 1 1-.25 11.4 11.4 0 0 0 3.6.57 1 1 0 0 1 1 1V20a1 1 0 0 1-1 1A17 17 0 0 1 3 4a1 1 0 0 1 1-1h3.5a1 1 0 0 1 1 1c0 1.25.2 2.45.57 3.6a1 1 0 0 1-.25 1Z" fill="var(--teal-dark)"/></svg>
    </div>
    <p class="phone-number">08 9351 4276</p>
    <p class="cta-meta">www.bravonclinic.com.au &nbsp;|&nbsp; near Tallowmere shopping centre</p>
  </section>

  <p class="tagline">Eat Better. Feel Better. Smile with Confidence Again.</p>

</main>
</body>
</html>
```